Business Card Design - Property Management & Real Estate Services

I need a business card design for my company that I can print Pell Prints. The company is called Tarrow Management Company. It is a property management and real estate company. The design has to be clean and modern. I need two versions. One for my employee and one for me. However, the design will be the same, just different text. You can get a feel for the company by looking at our website at www.tarrowmanagement.example.

Industry/Entity Type

Property Management

Contact Information for Business Card

I will be using Pell.com to print my cards. I will most likely use the rounded edges card. I need two versions, however, they will be the same design. I need one for me and my employee.

Colors
3276b5
33a6d7

Requirements
Must have
• Company Logo
• Name of person
• Property Management & Real Estate Service
• Phone
• Email
• Website
• Address
• A space to place a QR code

```html
<!DOCTYPE html>
<html lang="en">
<head>
<meta charset="utf-8">
<title>Tarrow Management – Business Card</title>
<link rel="stylesheet" href="https://fonts.googleapis.com/css2?family=Roboto:wght@400;500;700&display=swap">
<style>
  :root {
    --backdrop: #3a3a3c;
    --card-black: #1c1d20;
    --card-black-soft: #232428;
    --silver: #c9ccd1;
    --silver-dim: #8d9096;
    --brand-blue: #1b56a8;
    --accent-sky: #6fa3dc;
    --logo-blue: #3a7ac4;
    --text-white: #ffffff;
    --text-muted: #dbe5f3;
  }
  * { box-sizing: border-box; margin: 0; padding: 0; }
  html, body {
    width: 799px; height: 1200px; overflow: hidden;
    background: var(--backdrop);
    font-family: "Roboto", Arial, sans-serif;
  }
  .canvas { position: relative; width: 799px; height: 1200px; }
  .card {
    position: absolute; left: 100px; width: 600px; height: 340px;
    border-radius: 26px; overflow: hidden;
  }

  /* Front */
  .card-front {
    top: 110px;
    background: var(--card-black);
    display: flex; flex-direction: column; align-items: center; justify-content: center;
    gap: 14px;
  }
  .front-wordmark {
    color: var(--silver);
    font-weight: 500; font-size: 42px; letter-spacing: 3px;
    text-transform: uppercase;
  }
  .front-tagline {
    color: var(--silver-dim);
    font-size: 13px; letter-spacing: 3px; text-transform: uppercase;
  }

  /* Back */
  .card-back { top: 720px; background: var(--brand-blue); }
  .back-band {
    position: absolute; left: 0; top: 0; width: 100%; height: 112px;
    background: var(--card-black-soft);
  }
  .back-wordmark {
    position: absolute; left: 34px; top: 30px;
    color: var(--logo-blue);
    font-weight: 500; font-size: 28px; letter-spacing: 2px;
    text-transform: uppercase;
  }
  .back-tagline {
    position: absolute; left: 34px; top: 70px;
    color: var(--silver);
    font-size: 12px; letter-spacing: 1.5px; text-transform: uppercase;
  }
  .accent-stripe {
    position: absolute; left: 0; bottom: 22px; width: 100%; height: 8px;
    background: var(--accent-sky);
  }
  .holder { position: absolute; left: 34px; top: 128px; color: var(--text-white); }
  .holder-name { font-weight: 700; font-size: 24px; }
  .holder-role { font-size: 14px; color: var(--text-muted); margin-top: 2px; }
  .contact-list {
    position: absolute; left: 34px; top: 192px; list-style: none;
    color: var(--text-white); font-size: 15px;
  }
  .contact-list li { display: flex; align-items: center; gap: 10px; height: 24px; white-space: nowrap; }
  .contact-list svg { width: 14px; height: 14px; fill: var(--text-white); flex: none; }

  .qr-space {
    position: absolute; right: 40px; top: 132px; width: 150px; height: 150px;
    border: 4px solid var(--accent-sky); border-radius: 10px;
    background: rgba(255,255,255,0.06);
  }
</style>
</head>
<body>
<main class="canvas">
  <section class="card card-front" aria-label="Card front">
    <span class="front-wordmark">Tarrow Management</span>
    <span class="front-tagline">Property Management &amp; Real Estate Service</span>
  </section>

  <section class="card card-back" aria-label="Card back">
    <div class="back-band"></div>
    <span class="back-wordmark">Tarrow Management</span>
    <span class="back-tagline">Property Management &amp; Real Estate Service</span>

    <div class="holder">
      <p class="holder-name">Dario M. Ferrante</p>
      <p class="holder-role">Founder</p>
    </div>

    <ul class="contact-list">
      <li>
        <svg viewBox="0 0 16 16" aria-hidden="true"><path d="M3.5 1.5l2.5 0 1 3.5-1.6 1.2a8 8 0 0 0 4.4 4.4L11 9l3.5 1v2.5c0 1-1 2-2 2A11 11 0 0 1 1.5 3.5c0-1 1-2 2-2z"/></svg>
        (555) 014-2876
      </li>
      <li>
        <svg viewBox="0 0 16 16" aria-hidden="true"><path d="M1 3h14v10H1z M1.8 3.8L8 8.6l6.2-4.8" fill="none" stroke="#fff" stroke-width="1.6"/></svg>
        dario@tarrowmanagement.example
      </li>
      <li>
        <svg viewBox="0 0 16 16" aria-hidden="true"><g fill="none" stroke="#fff" stroke-width="1.4"><circle cx="8" cy="8" r="6.3"/><ellipse cx="8" cy="8" rx="2.8" ry="6.3"/><path d="M1.7 8h12.6"/></g></svg>
        www.tarrowmanagement.example
      </li>
      <li>480 Harbor Lane #210 Bayview, FL 30000</li>
    </ul>

    <div class="qr-space" role="img" aria-label="Space reserved for QR code"></div>
    <div class="accent-stripe"></div>
  </section>
</main>
</body>
</html>
```